Brochure for Veterinary Acupuncture and Physical Therapy
Willow Creek Pet Clinic
Putting the heart into healing
I am a veterinarian. My business is to travel from between existing veterinary practices to do acupucture and physical therapy with dogs and cats. This brochure will be something for the veterinary clinic to give their client about this service.
Animals
Veterinary pet owners
3 fold brochure
Photos and logo. Text will be coming in a separate upload. I'm not sure how much text is appropriate, so for now, can you put empty text boxes in designs so I can see how it might lay out? One section should be about me (picture of me with the dog), one section about acupuncture and one about physical therapy. Then another text box about how to schedule an appointment.
Me
Physical therapy picture
website: willowcreekpetclinic.net
email: willowcreekvet@postbloom.net
Also needs a facebook symbol
My business card, if that helps
Conditions treated -- depending on space I can shorten the physical therapy information
Overview
This is about me
Scheduling
New "training"
New mission

```html
<!DOCTYPE html>
<html lang="en">
<head>
<meta charset="utf-8">
<title>Willow Creek Pet Clinic – Tri-fold Brochure</title>
<link href="https://fonts.googleapis.com/css2?family=Open+Sans:wght@400;600;700&display=swap" rel="stylesheet">
<style>
:root{
  --bg:#ecebe8;
  --paper:#ffffff;
  --purple:#4a2c86;
  --purple-dark:#36206a;
  --green:#3fa535;
  --teal:#1aa39c;
  --blue:#2a62ad;
  --ink:#333333;
  --muted:#666666;
}
*{margin:0;padding:0;box-sizing:border-box}
html,body{width:1200px;height:562px;overflow:hidden;background:var(--bg);font-family:"Open Sans",Arial,sans-serif;color:var(--ink)}
.sheet{position:absolute;top:58px;width:576px;height:446px;background:var(--paper);box-shadow:0 2px 8px rgba(0,0,0,.18);overflow:hidden}
.sheet--outside{left:16px}
.sheet--inside{left:608px}
.panel{position:absolute;top:0;width:192px;height:446px}
.panel:nth-child(1){left:0}.panel:nth-child(2){left:192px}.panel:nth-child(3){left:384px}
.photo{position:absolute}
.brand{font-weight:700;color:var(--purple);font-size:13px;line-height:1.15;display:flex;align-items:center;gap:6px}
.brand .dot{width:10px;height:10px;border-radius:50%;background:var(--green);flex:none}
.tagline{font-size:7px;color:var(--green);font-weight:600;margin-top:3px;letter-spacing:.3px}
.body{font-size:7px;line-height:1.5;color:var(--ink)}
h2{font-size:8px;font-weight:700;color:var(--purple);margin-bottom:4px}
.list{list-style:none;font-size:7px;line-height:1.65}
.list li::before{content:"";display:inline-block;width:4px;height:4px;background:var(--green);border-radius:50%;margin-right:5px;vertical-align:middle}
/* outside */
.about .photo{left:0;top:0;width:192px;height:200px;background:linear-gradient(160deg,#9c7f63,#d8c7b3 60%,#b49a7e)}
.about .text{position:absolute;left:16px;top:214px;width:160px}
.contact-panel .rule{position:absolute;right:0;top:0;width:14px;height:446px;background:var(--purple)}
.contact-panel .block{position:absolute;left:20px;top:300px;width:150px}
.contact-panel .lines{margin-top:14px;font-size:7px;line-height:1.7;color:var(--purple)}
.social{display:flex;align-items:center;gap:5px;margin-top:4px}
.social .sq{width:10px;height:10px;background:var(--blue)}
.cover .band{position:absolute;left:0;top:0;width:192px;height:26px;background:var(--purple)}
.cover .logo-area{position:absolute;left:16px;top:44px;width:162px}
.cover .photo{left:0;top:110px;width:192px;height:270px;background:linear-gradient(170deg,#8f7a63,#cbb89f 55%,#6e5a48)}
.cover .foot{position:absolute;left:0;bottom:0;width:192px;height:66px;background:var(--purple);color:#fff;font-size:8px;font-weight:600;display:flex;align-items:center;justify-content:center;border-top:5px solid var(--green)}
/* inside */
.acu .top{position:absolute;left:14px;top:16px;width:164px}
.acu .text{position:absolute;left:14px;top:74px;width:164px}
.acu .text p+p{margin-top:6px}
.acu .photo{left:0;top:236px;width:192px;height:210px;background:linear-gradient(150deg,#b9a58b,#e3d7c6 55%,#9b8468)}
.conditions .strip{left:0;top:0;width:192px;height:46px;background:linear-gradient(90deg,#3fa535,#7fc66a)}
.conditions .head{position:absolute;left:0;top:46px;width:192px;height:50px;background:var(--teal);color:#fff;font-size:10px;font-weight:700;line-height:1.25;padding:9px 14px}
.conditions .list{position:absolute;left:16px;top:104px}
.conditions .photo{left:0;top:278px;width:192px;height:86px;background:linear-gradient(120deg,#a58b70,#d9c8b4)}
.conditions .sched{position:absolute;left:14px;top:370px;font-size:9px;font-weight:700;color:var(--purple)}
.rehab .photo{left:0;top:0;width:192px;height:118px;background:linear-gradient(180deg,#7eb8de,#c9dfeb 60%,#6aa455)}
.rehab h3{position:absolute;left:14px;top:126px;width:168px;font-size:10px;font-weight:700;color:var(--green);line-height:1.25}
.rehab .list{position:absolute;left:16px;top:164px}
.rehab .note{position:absolute;left:14px;top:300px;width:164px;background:var(--green);color:#fff;font-size:8px;font-weight:600;padding:8px 10px;line-height:1.4}
.schedule-band{position:absolute;left:192px;bottom:0;width:384px;height:40px;background:var(--blue);color:#fff;display:flex;align-items:center;justify-content:space-between;padding:0 14px;font-size:7px;line-height:1.4}
.schedule-band .msg{width:170px}
.schedule-band .links{text-align:right;font-weight:600}
</style>
</head>
<body>
<section class="sheet sheet--outside">
  <article class="panel about">
    <div class="photo" role="img" aria-label="Veterinarian sitting with a large shaggy dog"></div>
    <div class="text">
      <h2>ABOUT YOUR VETERINARIAN</h2>
      <p class="body">I travel between local veterinary practices to bring acupuncture and physical therapy to dogs and cats. My goal is gentle, whole-body care that helps each pet move, rest and heal with comfort. I work with your family vet to plan every visit.</p>
    </div>
  </article>
  <article class="panel contact-panel">
    <div class="rule"></div>
    <div class="block">
      <div class="brand"><span class="dot"></span>Willow Creek Pet Clinic</div>
      <div class="tagline">PUTTING THE HEART INTO HEALING</div>
      <div class="lines">
        <p>willowcreekvet@postbloom.net</p>
        <p>willowcreekpetclinic.net</p>
        <div class="social"><span class="sq"></span><span>Follow us</span></div>
      </div>
    </div>
  </article>
  <article class="panel cover">
    <div class="band"></div>
    <div class="logo-area">
      <div class="brand"><span class="dot"></span>Willow Creek Pet Clinic</div>
      <div class="tagline">PUTTING THE HEART INTO HEALING</div>
    </div>
    <div class="photo" role="img" aria-label="Portrait of a husky-mix dog"></div>
    <div class="foot">willowcreekpetclinic.net</div>
  </article>
</section>

<section class="sheet sheet--inside">
  <article class="panel acu">
    <div class="top">
      <div class="brand"><span class="dot"></span>Willow Creek Pet Clinic</div>
      <div class="tagline">PUTTING THE HEART INTO HEALING</div>
    </div>
    <div class="text body">
      <p>Acupuncture is a gentle therapy that uses fine needles at chosen points to ease pain, calm the body and support natural healing. Most pets relax during treatment and many fall asleep.</p>
      <p>Sessions last about thirty minutes and can be combined with medicine, diet changes or physical therapy for the best result.</p>
    </div>
    <div class="photo" role="img" aria-label="Small dog resting during an acupuncture session"></div>
  </article>
  <article class="panel conditions">
    <div class="photo strip" role="img" aria-label="Green grassy banner image"></div>
    <div class="head">Conditions Commonly Treated with Acupuncture</div>
    <ul class="list">
      <li>Arthritis</li><li>Hip dysplasia</li><li>Back and neck pain</li><li>Disc disease</li><li>Nerve injury</li><li>Skin allergies</li><li>Digestive upset</li><li>Kidney disease</li><li>Anxiety</li><li>Senior wellness</li>
    </ul>
    <div class="photo" role="img" aria-label="Veterinarian with a dog during treatment"></div>
    <div class="sched">Scheduling an appointment:</div>
  </article>
  <article class="panel rehab">
    <div class="photo" role="img" aria-label="Dog leaping over an agility jump"></div>
    <h3>Veterinary physical therapy and rehabilitation can treat:</h3>
    <ul class="list">
      <li>Recovery after surgery</li><li>Joint and muscle strain</li><li>Weakness in older pets</li><li>Weight and fitness goals</li><li>Nerve and spine problems</li><li>Sports and agility injuries</li>
    </ul>
    <p class="note">Please ask us how rehab can help your pet feel their best!</p>
  </article>
  <div class="schedule-band">
    <p class="msg">Ask your veterinarian for a referral, or contact us directly to book a visit at your clinic.</p>
    <div class="links"><p>willowcreekvet@postbloom.net</p><p>willowcreekpetclinic.net</p></div>
  </div>
</section>
</body>
</html>
```